100% West Australian Static Banner

I require a static banner to go on a couple of pages in our website (under development) that highlights that we are a 100% Western Australian Owned & Operated company. I would prefer the banner to be in our company colours (blue shades & grey). I also would like it to be eye catching and modern in design. I have included a 100% West Australian rubber stamp logo to be used as well as including our logo so you know our colours. The banner needs to be 1139 x 350 pixels in size.

Target Market(s)

B2B

Requirements
Must have
• Our rubber stamp 100% West Australian logo
• Modern Eye Catching design
• Blue shaded background
Nice to have
• Shading background similar our logo blue colours
• 100% logo can be reversed out if required or colour changed
• Larger text saying - 100% West Australian Owned & Operated

```html
<!DOCTYPE html>
<html lang="en">
<head>
<meta charset="utf-8">
<title>100% West Australian Owned &amp; Operated Banner</title>
<link rel="stylesheet" href="https://fonts.googleapis.com/css2?family=Oswald:wght@500&family=Montserrat:wght@400&display=swap">
<style>
  :root {
    --navy-deep: #050f24;
    --navy: #0c2350;
    --navy-glow: #17386f;
    --map-dark: #3b3c3f;
    --map-mid: #75787d;
    --map-light: #9a9da2;
    --white: #ffffff;
    --flare: #4aa6ff;
    --brand-grey: #9aa0a8;
    --brand-blue: #2e6fc4;
  }
  * { margin: 0; padding: 0; box-sizing: border-box; }
  html, body {
    width: 1200px;
    height: 370px;
    overflow: hidden;
    background: var(--navy-deep);
  }
  .banner {
    position: relative;
    width: 1200px;
    height: 370px;
    overflow: hidden;
    background: var(--navy-deep);
  }
  .banner__backdrop {
    position: absolute;
    inset: 0;
  }
  .banner__flare {
    position: absolute;
    left: 330px;
    top: 188px;
    width: 280px;
    height: 60px;
    background: radial-gradient(ellipse at center, rgba(200,230,255,0.95) 0%, rgba(74,166,255,0.6) 16%, rgba(74,166,255,0) 65%);
  }
  .headline__figure {
    position: absolute;
    left: 58px;
    top: 72px;
    font-family: "Oswald", sans-serif;
    font-weight: 500;
    font-size: 185px;
    line-height: 1;
    letter-spacing: -4px;
    color: var(--white);
    transform: scaleX(0.88);
    transform-origin: left top;
    text-shadow: 0 4px 14px rgba(0,0,0,0.45);
  }
  .headline__region {
    position: absolute;
    left: 442px;
    top: 157px;
    font-family: "Oswald", sans-serif;
    font-weight: 500;
    font-size: 57px;
    line-height: 1;
    color: var(--white);
    white-space: nowrap;
    transform: scaleX(0.845);
    transform-origin: left top;
    text-shadow: 0 3px 10px rgba(0,0,0,0.4);
  }
  .headline__tagline {
    position: absolute;
    left: 444px;
    top: 218px;
    font-family: "Montserrat", sans-serif;
    font-weight: 400;
    font-size: 22px;
    line-height: 1;
    letter-spacing: 10.5px;
    color: var(--white);
    white-space: nowrap;
  }
  .stamp {
    position: absolute;
    left: 895px;
    top: 64px;
    width: 200px;
    height: 200px;
  }
  .brand {
    position: absolute;
    left: 887px;
    top: 274px;
    display: flex;
    align-items: center;
    gap: 10px;
  }
  .brand__mark {
    width: 44px;
    height: 44px;
    border-radius: 50%;
    background: var(--brand-blue);
  }
  .brand__name {
    font-family: "Oswald", sans-serif;
    font-weight: 500;
    font-size: 26px;
    color: var(--brand-grey);
  }
</style>
</head>
<body>
  <div class="banner">
    <svg class="banner__backdrop" width="1200" height="370" viewBox="0 0 1200 370" aria-hidden="true">
      <defs>
        <radialGradient id="navy-tone" cx="0.75" cy="0.3" r="0.7">
          <stop offset="0" stop-color="#17386f"/>
          <stop offset="0.55" stop-color="#0b1e45"/>
          <stop offset="1" stop-color="#050f24"/>
        </radialGradient>
        <linearGradient id="map-tone" x1="0" y1="0" x2="1" y2="0.4">
          <stop offset="0" stop-color="#3b3c3f"/>
          <stop offset="0.45" stop-color="#75787d"/>
          <stop offset="1" stop-color="#5d6065"/>
        </linearGradient>
      </defs>
      <rect width="1200" height="370" fill="url(#navy-tone)"/>
      <path d="M878 0 C790 150 590 300 350 370 L395 370 C630 300 830 150 915 0 Z" fill="#6f7379" opacity="0.55"/>
      <g role="img" aria-label="Textured map of Western Australia in grey tones">
        <path d="M0 0 H878 C790 150 590 300 350 370 H0 Z" fill="url(#map-tone)"/>
      </g>
    </svg>

    <div class="banner__flare"></div>

    <div class="headline">
      <span class="headline__figure">100%</span>
      <div class="headline__region">WEST AUSTRAILIAN</div>
      <div class="headline__tagline">OWNED &amp; OPERATED</div>
    </div>

    <svg class="stamp" viewBox="0 0 200 200" role="img" aria-label="Locally owned seal">
      <circle cx="100" cy="100" r="98" fill="var(--white)"/>
      <circle cx="100" cy="100" r="80" fill="none" stroke="var(--navy)" stroke-width="6"/>
      <circle cx="100" cy="100" r="66" fill="var(--white)" stroke="var(--navy)" stroke-width="2"/>
    </svg>

    <div class="brand">
      <span class="brand__mark"></span>
      <span class="brand__name">Harbourline Packing</span>
    </div>
  </div>
</body>
</html>
```